Dune Business Card Design Project

We have an existing business card. We are looking to creat a new card for the store. I have attached a my own business so you have a refference of what the current card looks like.

Phone: 1300 574 213
email: merrow@dunepanes.com.au
website: www.dunepanes.com.au
Address: (Inside Merrow Rug Hall) 418 Tolvey Rd, Pelbrook VIC 3158
Updates

This is a new business card for our store.

Industry/Entity Type

Business

Requirements
Must have
• Must look similar to the existing card

```html
<!DOCTYPE html>
<html lang="en">
<head>
<meta charset="utf-8">
<title>Dune Shutters &amp; Blinds – Business Card</title>
<link rel="stylesheet" href="https://fonts.googleapis.com/css2?family=Open+Sans:wght@400;600;700&display=swap">
<style>
  :root {
    --backdrop: #e9e6e1;
    --card-white: #ffffff;
    --card-grey: #6c6d70;
    --ink: #231f20;
    --ink-soft: #58595b;
    --ink-muted: #8a8b8d;
    --rule: #9c9d9f;
    --on-grey: #ffffff;
  }
  * { box-sizing: border-box; margin: 0; padding: 0; }
  html, body { width: 1200px; height: 900px; overflow: hidden; }
  body {
    background: var(--backdrop);
    font-family: "Open Sans", Arial, sans-serif;
    display: flex;
    align-items: center;
    justify-content: center;
    gap: 40px;
  }
  .card {
    position: relative;
    width: 560px;
    height: 320px;
    border-radius: 3px;
    box-shadow: 0 6px 18px rgba(0,0,0,0.18);
    overflow: hidden;
  }
  /* Front */
  .card--front { background: var(--card-white); color: var(--ink); }
  .brand {
    position: absolute;
    left: 34px;
    top: 62px;
  }
  .brand__name {
    font-weight: 600;
    font-size: 74px;
    line-height: 1;
    letter-spacing: 1px;
    color: var(--ink);
  }
  .brand__tagline {
    font-weight: 700;
    font-size: 21px;
    color: var(--ink-soft);
    margin-top: 4px;
    letter-spacing: 0.3px;
  }
  .divider {
    position: absolute;
    left: 0;
    right: 0;
    top: 180px;
    height: 1px;
    background: linear-gradient(to right, rgba(156,157,159,0), var(--rule) 30%, var(--rule));
  }
  .person {
    position: absolute;
    right: 30px;
    top: 150px;
    text-align: right;
  }
  .person__name { font-weight: 700; font-size: 17px; color: var(--ink); }
  .person__role { font-size: 11px; color: var(--ink-muted); margin-top: 10px; }
  .contact {
    position: absolute;
    right: 30px;
    top: 218px;
    list-style: none;
    text-align: right;
    font-size: 12.5px;
    color: var(--ink-soft);
    line-height: 1.65;
  }
  .contact__item { display: flex; justify-content: flex-end; align-items: center; gap: 6px; }
  .contact__icon { width: 11px; height: 11px; fill: none; stroke: var(--ink-soft); stroke-width: 1.3; }
  .address {
    position: absolute;
    left: 34px;
    bottom: 34px;
    font-style: normal;
    font-size: 14px;
    line-height: 1.45;
    color: var(--ink-soft);
  }
  /* Back */
  .card--back {
    background: var(--card-grey);
    color: var(--on-grey);
  }
  .back__name {
    position: absolute;
    left: 110px;
    top: 60px;
    font-weight: 400;
    font-size: 140px;
    line-height: 1;
    letter-spacing: 2px;
  }
  .back__web {
    position: absolute;
    left: 130px;
    top: 232px;
    font-weight: 700;
    font-size: 22px;
  }
</style>
</head>
<body>
  <section class="card card--front" aria-label="Card front">
    <div class="brand">
      <div class="brand__name">dune</div>
      <div class="brand__tagline">Shutters &amp; Blinds</div>
    </div>
    <div class="person">
      <div class="person__name">Tobias Renn</div>
      <div class="person__role">Director</div>
    </div>
    <div class="divider"></div>
    <ul class="contact">
      <li class="contact__item">
        <svg class="contact__icon" viewBox="0 0 12 12"><circle cx="6" cy="6" r="5"/><path d="M4 3.5c0 3 1.5 4.5 4.5 5l.5-1.3-1.4-.6-.6.7c-1-.4-1.6-1-2-2l.7-.6-.6-1.4z" stroke-width="0.8"/></svg>
        1300 574 213
      </li>
      <li class="contact__item">
        <svg class="contact__icon" viewBox="0 0 12 12"><rect x="1" y="2.5" width="10" height="7" rx="0.8"/><path d="M1 3l5 3.6L11 3"/></svg>
        merrow@dunepanes.com.au
      </li>
      <li class="contact__item">
        <svg class="contact__icon" viewBox="0 0 12 12"><circle cx="6" cy="6" r="5"/><ellipse cx="6" cy="6" rx="2.2" ry="5"/><path d="M1 6h10"/></svg>
        www.dunepanes.com.au
      </li>
    </ul>
    <address class="address">418 Tolvey Rd<br>Pelbrook VIC 3158</address>
  </section>

  <section class="card card--back" aria-label="Card back">
    <div class="back__name">dune</div>
    <div class="back__web">www.dunepanes.com.au</div>
  </section>
</body>
</html>
```